Letterhead and Envelopes design using existing logo. Logo can be found at tlventures.net

Use existing logo (attached) and incorporate in letterhead and envelope designs.

Current logo can be viewed at tlventures.net the web site reflect various parent and sub companies. Please see attached as well.

Target Market(s)

Other oil and gas operators.

Industry/Entity Type

Oil And Gas

Font styles to use
Sans Serif

Colors

Designer to choose colors to be used in the design.

Requirements
Must have
• Current logo and address
Nice to have
• Modern, contemporary approach yet incorporate existing traditional design.
• After design is selected for Ridgemont Caldera Holdings I will use similar design for Royalties, Exploration, Energy and Farms with different color schemes.

```html
<!DOCTYPE html>
<html lang="en">
<head>
<meta charset="utf-8">
<title>Ridgemont Caldera Holdings – Stationery</title>
<link href="https://fonts.googleapis.com/css2?family=Open+Sans:wght@400;600;700&display=swap" rel="stylesheet">
<style>
  :root {
    --bg: #f5f6f8;
    --paper: #ffffff;
    --green: #6e9a3f;
    --ink: #5a5a5a;
    --ink-dark: #222222;
  }
  * { box-sizing: border-box; margin: 0; padding: 0; }
  html, body { width: 1200px; height: 1200px; overflow: hidden; }
  body {
    position: relative;
    background: var(--bg);
    font-family: "Open Sans", Arial, sans-serif;
    color: var(--ink);
  }
  .sheet { position: absolute; background: var(--paper); }

  /* Letterhead */
  .letterhead { left: 162px; top: 254px; width: 497px; height: 712px; }
  .brand { position: absolute; display: flex; align-items: center; gap: 8px; }
  .brand-dot { border-radius: 50%; background: var(--green); flex: none; }
  .brand-name { font-weight: 700; color: var(--ink-dark); line-height: 1.15; }
  .letterhead .brand { left: 56px; top: 44px; }
  .letterhead .brand-dot { width: 22px; height: 22px; }
  .letterhead .brand-name { font-size: 13px; width: 120px; }

  .sender-address {
    position: absolute; right: 51px; top: 52px;
    text-align: right; font-size: 12px; line-height: 13.5px;
    letter-spacing: 0.6px; font-style: normal;
  }
  .salutation {
    position: absolute; left: 56px; top: 176px;
    font-size: 13px; font-weight: 700;
  }
  .letter-body { position: absolute; left: 56px; top: 200px; width: 392px; }
  .letter-body p {
    font-size: 11.4px; line-height: 13.3px; margin-bottom: 17px;
  }
  .signature {
    position: absolute; left: 363px; top: 540px; width: 80px;
    text-align: center; font-size: 12.8px; color: #333;
  }
  .signature-line {
    position: absolute; left: 363px; top: 576px; width: 80px;
    border-top: 1px solid #333;
  }
  .contact {
    position: absolute; display: flex; align-items: center; gap: 4px;
    color: var(--green); font-weight: 600; white-space: nowrap;
  }
  .contact svg { fill: var(--green); flex: none; }
  .letterhead .contact { top: 666px; font-size: 8.4px; }
  .letterhead .contact svg { width: 8px; height: 8px; }
  .band {
    position: absolute; background: var(--green);
  }
  .letterhead .band { left: 0; top: 688px; width: 497px; height: 24px; border-radius: 0 12px 12px 0; }

  /* Envelope back */
  .envelope-back { left: 640px; top: 400px; width: 386px; height: 200px; }
  .envelope-back .flap { position: absolute; left: 0; top: 0; }
  .envelope-back .web {
    position: absolute; left: 0; right: 0; top: 182px;
    text-align: center; font-size: 6.4px; font-weight: 600; color: var(--green);
  }

  /* Envelope front */
  .envelope-front { left: 638px; top: 638px; width: 388px; height: 202px; }
  .envelope-front .brand { left: 12px; top: 20px; gap: 5px; }
  .envelope-front .brand-dot { width: 12px; height: 12px; }
  .envelope-front .brand-name { font-size: 7px; width: 62px; }
  .envelope-front .contact { top: 172px; font-size: 6.4px; gap: 3px; }
  .envelope-front .contact svg { width: 6px; height: 6px; }
  .envelope-front .band { left: 0; top: 186px; width: 388px; height: 14px; border-radius: 0 7px 7px 0; }
</style>
</head>
<body>

<section class="sheet letterhead" aria-label="Letterhead">
  <div class="brand">
    <span class="brand-dot"></span>
    <span class="brand-name">Ridgemont Caldera Holdings</span>
  </div>
  <address class="sender-address">840 Granite Way,<br>Ashford<br>58119</address>

  <p class="salutation">Dear Mr.--------</p>
  <div class="letter-body">
    <p>Lorem Ipsum is simply dummy text of the printing and typesetting industry. Lorem Ipsum has been the industry's standard dummy text ever since the 1500s, when an unknown printer took a galley of type and scrambled it to make a type specimen book. It has survived not only five centuries, but also the leap into electronic typesetting, remaining essentially unchanged. It was popularised in the 1960s with the release of Letraset sheets containing Lorem Ipsum passages, and more recently with desktop publishing software like Aldus PageMaker including versions of Lorem Ipsum.</p>
    <p>Lorem Ipsum is simply dummy text of the printing and typesetting industry. Lorem Ipsum has been the industry's standard dummy text ever since the 1500s, when an unknown printer took a galley of type and scrambled it to make a type specimen book. It has survived not only five centuries, but also the leap into electronic typesetting, remaining essentially unchanged. It was popularised in the 1960s with the release of Letraset sheets containing Lorem Ipsum passages, and more recently with desktop publishing software like Aldus PageMaker including versions of Lorem Ipsum.</p>
  </div>

  <p class="signature">Signature</p>
  <div class="signature-line"></div>

  <div class="contact" style="left:40px">
    <svg viewBox="0 0 10 10"><path d="M2 0.5 L3.6 2.6 L2.8 3.7 Q4 6 6.3 7.2 L7.4 6.4 L9.5 8 L8.4 9.5 Q3.5 9 0.5 1.6 Z"/></svg>
    <span>(555) 013.4471</span>
  </div>
  <div class="contact" style="left:190px">
    <svg viewBox="0 0 10 10"><path d="M0 2 H10 V8.5 H0 Z" /><path d="M0.4 2.4 L5 5.6 L9.6 2.4" stroke="#fff" stroke-width="0.9" fill="none"/></svg>
    <span>reception@tlventures.net</span>
  </div>
  <div class="contact" style="left:366px">
    <svg viewBox="0 0 10 10"><circle cx="5" cy="5" r="4.6"/><path d="M0.6 5 H9.4 M5 0.5 Q2 5 5 9.5 M5 0.5 Q8 5 5 9.5" stroke="#fff" stroke-width="0.8" fill="none"/></svg>
    <span>www.tlventures.net</span>
  </div>
  <div class="band"></div>
</section>

<section class="sheet envelope-back" aria-label="Envelope back">
  <svg class="flap" width="386" height="40" viewBox="0 0 386 40">
    <path d="M0 0 H386 L351 29 Q338 38 322 38 H64 Q48 38 35 29 Z" fill="var(--green)"/>
  </svg>
  <p class="web">www.tlventures.net</p>
</section>

<section class="sheet envelope-front" aria-label="Envelope front">
  <div class="brand">
    <span class="brand-dot"></span>
    <span class="brand-name">Ridgemont Caldera Holdings</span>
  </div>
  <div class="contact" style="left:15px">
    <svg viewBox="0 0 10 10"><path d="M5 0 Q8.6 0 8.6 3.6 Q8.6 6 5 10 Q1.4 6 1.4 3.6 Q1.4 0 5 0 Z"/><circle cx="5" cy="3.6" r="1.4" fill="#fff"/></svg>
    <span>840 Granite Way, Ashford 58119</span>
  </div>
  <div class="contact" style="left:172px">
    <svg viewBox="0 0 10 10"><path d="M2 0.5 L3.6 2.6 L2.8 3.7 Q4 6 6.3 7.2 L7.4 6.4 L9.5 8 L8.4 9.5 Q3.5 9 0.5 1.6 Z"/></svg>
    <span>(555) 013.4471</span>
  </div>
  <div class="contact" style="left:280px">
    <svg viewBox="0 0 10 10"><path d="M0 2 H10 V8.5 H0 Z" /><path d="M0.4 2.4 L5 5.6 L9.6 2.4" stroke="#fff" stroke-width="0.9" fill="none"/></svg>
    <span>reception@tlventures.net</span>
  </div>
  <div class="band"></div>
</section>

</body>
</html>
```